Flyer-Design für  Kampfsportschule
Flyer-Design für Kampfsportschule
Zielgruppe
Wir bieten Taekwondo/Selbstverteidigung an. Meine Zielgruppe sind Erwachsene ab 17 Jahren.
Aufgabenstellung
Das Angebot '1 Monat kostenloses Training, oder einen Monat kostenloses Training' und 'Taekwondo/Selbstverteidigung in Weinstadt' soll eingebracht und direkt sichtbar sein. Eventuell auch Punkte wie Selbstbewusstsein, Beweglichkeit, Zielstrebigkeit, Kraft und Ausdauer, körperliche Fitness... Farben: Weiß, schwarz und Schrift in gelb. Nichts rotes.
Die Daten:
Tel: 0159-4817250 Email: t.m.budohalle@postwelle-mail.de und www.tmbudohalle.de

```html
<!DOCTYPE html>
<html lang="de">
<head>
<meta charset="utf-8">
<title>Flyer – T.M. Budohalle</title>
<link rel="stylesheet" href="https://fonts.googleapis.com/css2?family=Raleway:wght@700&family=Source+Sans+3:wght@400;600;700&display=swap">
<style>
  :root {
    --page-bg: #f3f3f4;
    --flyer-black: #1d1a1c;
    --accent-yellow: #f7c600;
    --text-on-yellow: #1d1a1c;
    --text-white: #ffffff;
    --photo-dark: #141214;
    --photo-light: #d9d6d4;
  }
  * { box-sizing: border-box; margin: 0; padding: 0; }
  html, body { width: 1200px; height: 817px; overflow: hidden; background: var(--page-bg); }
  body { position: relative; font-family: "Source Sans 3", "Source Sans Pro", sans-serif; color: var(--text-white); }

  .flyer {
    position: absolute; left: 417px; top: 28px;
    width: 365px; height: 760px;
    background: var(--flyer-black);
    overflow: hidden;
    box-shadow: 0 4px 14px rgba(0,0,0,.18);
  }

  .hero-photo {
    position: absolute; left: 168px; top: 42px; width: 197px; height: 336px;
    background: radial-gradient(ellipse at 55% 45%, var(--photo-light) 0%, #8e8a88 30%, var(--photo-dark) 70%);
    opacity: .9;
  }

  .brand {
    position: absolute; left: 20px; top: 36px;
    display: flex; align-items: center; gap: 10px;
  }
  .brand-dot { width: 28px; height: 28px; border-radius: 50%; background: var(--text-white); }
  .brand-name { font-weight: 700; font-size: 19px; letter-spacing: .5px; color: var(--text-white); }

  .headline { position: absolute; left: 21px; top: 213px; font-family: "Raleway", sans-serif; font-weight: 700; }
  .headline span {
    display: block; width: max-content;
    background: var(--accent-yellow); color: var(--text-on-yellow);
    font-size: 29px; line-height: 1; padding: 8px 10px;
  }
  .headline span + span { margin-top: 0; }

  .intro {
    position: absolute; left: 22px; top: 322px; width: 335px;
    font-size: 13.4px; line-height: 1.75; white-space: nowrap;
  }

  .question {
    position: absolute; left: 22px; top: 414px; width: 320px;
    font-size: 15.5px; font-weight: 700; line-height: 1.45;
  }
  .question em { font-style: normal; color: var(--accent-yellow); }

  .benefits {
    position: absolute; left: 22px; top: 474px; list-style: none;
    font-size: 14px; font-weight: 700;
  }
  .benefits li { position: relative; padding-left: 22px; height: 26px; line-height: 26px; }
  .benefits li::before {
    content: ""; position: absolute; left: 2px; top: 9px;
    width: 8px; height: 8px; border-radius: 50%; background: var(--accent-yellow);
  }

  .offer {
    position: absolute; left: 174px; top: 500px; width: 148px; height: 105px;
    border: 2px solid var(--accent-yellow);
    text-align: center; font-weight: 700; font-size: 23px; line-height: 1.1;
    padding-top: 11px;
  }
  .offer .offer-highlight { color: var(--accent-yellow); display: block; }

  .contact {
    position: absolute; left: 0; top: 638px; width: 365px; text-align: center;
    font-size: 14px; line-height: 1.75; font-style: normal;
  }
  .contact b { font-weight: 700; }

  .footer-band {
    position: absolute; left: 0; bottom: 0; width: 365px; height: 56px;
    background: var(--accent-yellow); color: var(--text-on-yellow);
    display: flex; align-items: center; justify-content: center;
    font-size: 14px; font-weight: 600;
  }
</style>
</head>
<body>
  <article class="flyer">
    <div class="hero-photo" role="img" aria-label="Foto einer Taekwondo-Kämpferin im weißen Dobok mit schwarzem Gürtel in Abwehrhaltung"></div>

    <div class="brand">
      <span class="brand-dot"></span>
      <span class="brand-name">T.M. BUDOHALLE</span>
    </div>

    <h1 class="headline">
      <span>Selbstverteidigung</span>
      <span>in Weinstadt</span>
    </h1>

    <p class="intro">Teste uns jetzt ganz unverbindlich in einem Probe-<br>training und lerne unsere Gruppe, sowie unsere<br>Trainer kennen und lass uns DEINE Ziele erreichen!</p>

    <p class="question">Was bekommen Sie, wenn Sie <em>Selbst-<br>verteidigung</em> lernen?</p>

    <ul class="benefits">
      <li>Selbstbewusstsein</li>
      <li>Beweglichkeit</li>
      <li>Selbstverteidigung</li>
      <li>Kraft und Ausdauer</li>
      <li>körperliche Fitness</li>
    </ul>

    <div class="offer">
      <span class="offer-highlight">1 Monat</span>
      kostenloses Training
    </div>

    <address class="contact">
      <div><b>Tel:</b> 0159-4817250</div>
      <div>t.m.budohalle@postwelle-mail.de</div>
    </address>

    <div class="footer-band">www.tmbudohalle.de</div>
  </article>
</body>
</html>
```